Leadership Brenvale Brochure Design*

We host a local leadership development program every two years. We need a brochure to promote the program. We would like it to be 8 1/2 x 11, tri-fold. I have attached a Word document with the necessary info for the brochure. The brochure will be professionally printed. We would like the final design to be in InDesign.

Target Market(s)

Potential participants of our leadership program. They will be local leaders, male and female, from 30-60 years of age.

Requirements
Must have
• Content as detailed in the Word document attached. Our logo.
Nice to have
• A design that is attractive to young professionals.

```html
<!DOCTYPE html>
<html lang="en">
<head>
<meta charset="utf-8">
<title>Leadership Brenvale – Program Brochure (inside spread)</title>
<link rel="stylesheet" href="https://fonts.googleapis.com/css2?family=Source+Sans+3:ital,wght@0,400;0,600;0,700;1,400;1,600;1,700&display=swap">
<style>
  :root {
    --ink: #1d1d22;
    --accent: #1f3fd4;
    --panel-left: #e5f3fc;
    --panel-mid: #ffffff;
    --panel-right: #d2e9f9;
    --photo-a: #3aa6a8;
    --photo-b: #8fd3cf;
    --rule: #1d1d22;
  }
  * { margin: 0; padding: 0; box-sizing: border-box; }
  html, body { width: 1200px; height: 927px; overflow: hidden; }
  body {
    font-family: "Source Sans 3", "Myriad Pro", sans-serif;
    color: var(--ink);
    position: relative;
    background: var(--panel-mid);
  }
  .panel { position: absolute; top: 0; height: 927px; }
  .panel--left { left: 0; width: 407px; background: var(--panel-left); }
  .panel--mid { left: 407px; width: 398px; background: var(--panel-mid); }
  .panel--right { left: 805px; width: 395px; background: var(--panel-right); }

  .block { position: absolute; }
  .heading { color: var(--accent); font-weight: 700; }
  .heading--section { font-size: 14.5px; }
  .heading--large { font-size: 17px; font-weight: 600; }

  .overview { left: 43px; top: 48px; width: 350px; }
  .overview p { font-size: 15px; line-height: 19.7px; margin-top: 4px; }
  .goals { list-style: none; margin: 9px 0 0 24px; }
  .goals li {
    position: relative; padding-left: 18px; font-size: 14.6px; font-weight: 600;
    line-height: 16.6px; margin-bottom: 8.5px;
  }
  .goals li svg { position: absolute; left: 0; top: 3px; }

  .session { position: absolute; width: 380px; }
  .session__date { position: absolute; left: 0; top: 0; color: var(--accent); font-weight: 700; font-size: 13.6px; }
  .session__body { margin-left: 84px; font-size: 13.2px; line-height: 16.4px; }
  .session__title { color: var(--accent); font-weight: 700; font-size: 13.6px; line-height: 16.4px; }
  .session__time { font-style: italic; }
  .session__time--plain { font-style: normal; }
  .session__note { font-weight: 700; }
  .topics { list-style: none; font-style: italic; margin-left: 10px; }
  .topics li { position: relative; padding-left: 10px; }
  .topics li::before { content: "●"; position: absolute; left: 0; font-style: normal; font-size: 9px; }
  .topics--small li::before { content: "•"; font-size: 11px; left: 0; }
  .topics--small { margin-left: 8px; }
  .topics--small li { padding-left: 17px; }

  .schedule-label { left: 43px; top: 397px; font-size: 15px; }

  .policy { left: 21px; width: 360px; }
  .policy p { font-size: 13.3px; line-height: 16.4px; margin-top: 3px; }
  .policy .em { font-style: italic; font-weight: 700; }

  .alumni-title { left: 0; width: 395px; top: 97px; text-align: center; font-size: 17px; font-weight: 600; }
  .quote { position: absolute; left: 25px; width: 333px; font-size: 13.3px; line-height: 19.7px; text-align: justify; }
  .quote p { margin: 0; }
  .portrait {
    float: left; width: 130px; height: 130px; border-radius: 50%;
    shape-outside: circle(50%); margin: 16px 10px 4px -7px;
    border: 1px solid var(--accent); padding: 3px; background-clip: content-box;
    background-image: radial-gradient(circle at 50% 40%, var(--photo-b), var(--photo-a));
  }
  .portrait--second { margin-top: 32px; }
  .signature { margin-top: 6px; text-align: left; }
  .signature b { font-weight: 700; }
  .divider { position: absolute; left: 37px; top: 384px; width: 320px; height: 12px; }
</style>
</head>
<body>

<section class="panel panel--left">
  <div class="block overview">
    <h2 class="heading heading--large">Program Overview</h2>
    <p>Leadership Brenvale is a leadership certification program designed to prepare the leaders of tomorrow. During the five-month program, participants get an in-depth view of community issues, develop leadership skills necessary to assume leadership roles, and are exposed to community involvement opportunities. Leadership Brenvale will provide participants with the opportunities to:</p>
    <ul class="goals">
      <li><svg width="12" height="11" viewBox="0 0 12 11"><path d="M1 6 L4.5 10 L11 1" fill="none" stroke="#1d1d22" stroke-width="1.4"/></svg>Build and demonstrate leadership and communication skills</li>
      <li><svg width="12" height="11" viewBox="0 0 12 11"><path d="M1 6 L4.5 10 L11 1" fill="none" stroke="#1d1d22" stroke-width="1.4"/></svg>Think critically about key business, policy, and civic issues facing Brenvale County</li>
      <li><svg width="12" height="11" viewBox="0 0 12 11"><path d="M1 6 L4.5 10 L11 1" fill="none" stroke="#1d1d22" stroke-width="1.4"/></svg>Build meaningful, long-lasting connections</li>
      <li><svg width="12" height="11" viewBox="0 0 12 11"><path d="M1 6 L4.5 10 L11 1" fill="none" stroke="#1d1d22" stroke-width="1.4"/></svg>Establish ongoing dialogues with experienced community leaders</li>
    </ul>
  </div>

  <h3 class="block heading schedule-label">Schedule:</h3>

  <div class="session" style="left:43px;top:415px;">
    <span class="session__date">January 17</span>
    <div class="session__body">
      <div class="session__title">Organizational Retreat &amp; Dinner</div>
      <div class="session__note">(Attendance Mandatory)</div>
      <div class="session__time session__time--plain">10:00 a.m. – 7:00 p.m.</div>
      <ul class="topics">
        <li>Introductions</li><li>Team Building</li><li>Motivation</li><li>Leadership Styles</li><li>Social Hour/Dinner</li>
      </ul>
    </div>
  </div>

  <div class="session" style="left:43px;top:562px;">
    <span class="session__date">January 31</span>
    <div class="session__body">
      <div class="session__title">Business &amp; Industry</div>
      <div class="session__time session__time--plain">8:30 a.m. – 4:00 p.m.</div>
      <ul class="topics">
        <li>Business &amp; Industry Panel</li><li>Tour of Ridgeline Manufacturing facility</li><li>Tour of Harlow Tool Company</li><li>“Taking your vision into B&amp;I”</li>
      </ul>
    </div>
  </div>

  <div class="session" style="left:43px;top:677px;">
    <span class="session__date">February 21</span>
    <div class="session__body">
      <div class="session__title">Education</div>
      <div class="session__time session__time--plain">8:30 a.m. – 4:00 p.m.</div>
      <ul class="topics">
        <li>Tour of selected programs at BCC</li><li>College Career Program overview</li><li>Lunch at Brenvale Career and College Academy</li><li>Tour of BCCA</li><li>Overview of CTE program paths</li>
      </ul>
    </div>
  </div>

  <div class="session" style="left:43px;top:825px;">
    <span class="session__date">March 14</span>
    <div class="session__body">
      <div class="session__title">Future Technologies &amp; Communications</div>
      <div class="session__time">8:30 a.m. – 4:00 p.m.</div>
      <ul class="topics"><li>BCC Presents interview</li></ul>
    </div>
  </div>
</section>

<section class="panel panel--mid">
  <div class="session" style="left:21px;top:49px;">
    <div class="session__body">
      <ul class="topics" style="margin-left:8px;"><li>Trends and forecasts</li><li>Marketing &amp; communications panel</li></ul>
    </div>
  </div>

  <div class="session" style="left:21px;top:90px;">
    <span class="session__date">April 4</span>
    <div class="session__body">
      <div class="session__title">Government</div>
      <div class="session__time">8:30 a.m. – 4:00 p.m.</div>
      <ul class="topics">
        <li>Overview of state/federal government</li><li>Overview of city/county government</li><li>Tour of Marston Correctional Institute</li><li>Tour of courthouse</li><li>Judicial presentations</li>
      </ul>
    </div>
  </div>

  <div class="session" style="left:21px;top:221px;">
    <span class="session__date">May 2</span>
    <div class="session__body">
      <div class="session__title">Health &amp; Wellness</div>
      <div class="session__time">8:30 a.m. – 4:00 p.m.</div>
      <ul class="topics">
        <li>Tour of Lower Valley Hospice</li><li>Community Wellness Roundtable</li><li>Tour of Ellison Cancer Care Center</li><li>Virtual Medicine Tutorial</li><li>Tour of BRHS</li>
      </ul>
    </div>
  </div>

  <div class="session" style="left:21px;top:352px;">
    <span class="session__date">May 18</span>
    <div class="session__body">
      <div class="session__title">Graduation Ceremony and Luncheon</div>
      <div class="session__time">(12:00 p.m.)</div>
      <ul class="topics topics--small">
        <li>Participants are encouraged to invite their employer/supervisor/mentor/special guest (x2)</li>
      </ul>
    </div>
  </div>

  <div class="block policy" style="top:455px;">
    <h2 class="heading heading--large">Attendance Policy</h2>
    <p>Attendance at all sessions including the opening retreat is compulsory. Participants may miss no more than one session to graduate; however, the Organizational Retreat is mandatory.</p>
  </div>

  <div class="block policy" style="top:558px;">
    <h2 class="heading heading--large">Tuition</h2>
    <p>If accepted in the Leadership Brenvale program, you or your employer/sponsor will be invoiced $400 for Chamber members and $500 for non-members. This fee covers costs for the retreat, classroom sessions, lunches, and graduation. No refunds will be provided for participants who drop out of the program or do not fulfill the required curriculum.</p>
  </div>

  <div class="block policy" style="top:694px;">
    <h2 class="heading heading--large">To Apply</h2>
    <p>Applications are available on the Chamber’s website,<br><span class="em">www.TheBrenvaleChamber.org</span><br><span class="em">Applications are due by November 2, 2020</span>.</p>
    <p>Class size is limited. All applications received by the deadline will be reviewed and final participants for the Leadership Brenvale class will be contacted on December 4, 2020. However, all applicants will be notified of the status of their application in writing.</p>
    <p style="margin-top:12px;"><span class="em">For questions, please call the Chamber, 555-014-2267</span>.</p>
  </div>
</section>

<section class="panel panel--right">
  <h2 class="block heading alumni-title">What Community alumni are saying</h2>

  <div class="quote" style="top:123px;">
    <p>“Leadership Brenvale was an awesome experience! I
    <span class="portrait" role="img" aria-label="Portrait photo of alumna Dana Whitlock"></span>
    learned many interesting things about the county that I have lived in all my life. We had very informative panel discussions and the tours of local attractions, including the Marston Correctional Facility were eye opening! I enjoyed learning and working beside a great group of folks who are taking leadership roles in our communities to make our county a better place to live, work and play.”</p>
    <p class="signature"><b>~Dana Whitlock, Co-Owner,</b> Fern’s Smokehouse</p>
  </div>

  <svg class="divider" viewBox="0 0 320 12" aria-hidden="true">
    <line x1="0" y1="6" x2="130" y2="6" stroke="#1d1d22" stroke-width="0.7"/>
    <line x1="190" y1="6" x2="320" y2="6" stroke="#1d1d22" stroke-width="0.7"/>
    <path d="M146 6 l4 -4 l4 4 l-4 4z M156 6 l4 -5 l4 5 l-4 5z M166 6 l4 -4 l4 4 l-4 4z" fill="#1d1d22"/>
  </svg>

  <div class="quote" style="top:409px;">
    <p>“For the first year and a half I was working at R. Calder Finch, I commuted from Port Ellery, so I was not involved in the community at all. Once we moved here, I knew I
    <span class="portrait portrait--second" role="img" aria-label="Portrait photo of alumnus Ben T. Harwell"></span>
    wanted and felt I had to become more involved. I learned about the program through a colleague. I couldn’t have asked for a better experience and it really exposed me to the many ways that I could get involved and contribute to the chamber and our community. I didn’t know a soul in that 2014 class when it started and now many of them are my very best friends. If you have an opportunity to go through Leadership Brenvale you would be crazy to pass it up. It is the best program the Chamber has and, quite frankly, one of the best opportunities to better yourself in this community.</p>
    <p class="signature" style="margin-top:10px;"><b>~Ben T. Harwell, CPA, Partner/Manager of the Millbrook Office,</b> R. Calder Finch &amp; Associates, LLP</p>
  </div>
</section>

</body>
</html>
```